Switch Kit - Banking Flyer

We want a design for an 8.5x11" flyer that matches the look of our website (www.morvalecommercebank.com). Outline is attached, but please feel free to include images/pictures/graphics that you think makes this easy to understand. The goal is to hand this flyer to a potential customer to get them to understand the information easily and quickly.

```html
<!DOCTYPE html>
<html lang="en">
<head>
<meta charset="utf-8">
<title>Switch Kit – Morvale Commerce Bank</title>
<link rel="stylesheet" href="https://fonts.googleapis.com/css2?family=Poppins:wght@400;500;600;700;800&display=swap">
<style>
  :root {
    --navy: #22426e;
    --gold: #8a5a14;
    --white: #ffffff;
    --ink: #111111;
    --backdrop: #cccccc;
  }
  * { margin: 0; padding: 0; box-sizing: border-box; }
  html, body { width: 1200px; height: 1000px; overflow: hidden; }
  body { background: var(--backdrop); font-family: 'Poppins', sans-serif; position: relative; }

  .flyer { position: absolute; left: 282px; top: 88px; width: 636px; height: 823px; background: var(--white); }
  .flyer > * { position: absolute; }

  .header { left: 0; top: 0; width: 636px; height: 202px; background: var(--navy); }
  .brand-name { left: 42px; top: 44px; width: 300px; color: var(--white); font-weight: 600; font-size: 24px; line-height: 28px; letter-spacing: 0.5px; text-align: center; }
  .brand-name span { display: block; font-size: 14px; font-weight: 600; letter-spacing: 3px; line-height: 20px; }
  .header-rule { left: 370px; top: 29px; width: 3px; height: 86px; background: var(--gold); }
  .headline { left: 385px; top: 34px; width: 230px; color: var(--white); text-align: center; font-weight: 800; }
  .headline .line1 { display: block; font-size: 21px; line-height: 30px; }
  .headline .line2 { display: block; font-size: 29px; line-height: 36px; }
  .intro { left: 29px; top: 126px; width: 579px; color: var(--white); font-size: 14.6px; line-height: 17.6px; text-align: justify; text-align-last: center; }

  .welcome { left: 20px; top: 217px; width: 596px; text-align: center; color: var(--ink); font-size: 17.5px; line-height: 22px; }
  .welcome strong { display: block; color: var(--gold); font-weight: 700; font-size: 18.5px; }

  .band { left: 0; width: 636px; height: 15px; background: var(--navy); }

  .step-badge { width: 33px; height: 33px; border-radius: 50%; background: var(--gold); color: var(--white); font-weight: 800; font-size: 22px; line-height: 33px; text-align: center; left: 11px; }
  .step-title { color: var(--gold); font-weight: 700; font-size: 15.5px; line-height: 19px; }
  .step-title.fit { font-size: 14px; white-space: nowrap; width: 318px; }
  .step-text { font-size: 12.6px; line-height: 15px; }
  .step-text.dark { color: var(--ink); text-align: justify; text-align-last: center; }
  .step-text.navy { color: var(--navy); }

  .photo { border-radius: 1px; }
  .photo.meeting { left: 384px; top: 302px; width: 224px; height: 132px; background: linear-gradient(135deg, #3b4a55 0%, #a8aaa6 45%, #c4824a 100%); }
  .photo.atm { left: 384px; top: 590px; width: 224px; height: 130px; background: linear-gradient(90deg, #1f3f7a 0%, #7a8c85 40%, #5f9e5a 75%, #b4d49a 100%); }

  .footer { left: 0; top: 735px; width: 636px; height: 88px; background: var(--navy); }
  .footer > * { position: absolute; }
  .pin-icon { left: 64px; top: 20px; }
  .address { left: 102px; top: 14px; color: var(--white); font-size: 14.8px; line-height: 17.5px; font-weight: 500; }
  .phone-icon { left: 386px; top: 22px; }
  .phone { left: 439px; top: 27px; color: var(--white); font-size: 22px; font-weight: 700; line-height: 28px; }
</style>
</head>
<body>
<main class="flyer">
  <header class="header"></header>
  <div class="brand-name">Morvale<span>Commerce Bank</span></div>
  <div class="header-rule"></div>
  <h1 class="headline"><span class="line1">SWITCHING IS EASY</span><span class="line2">AS 1-2-3!</span></h1>
  <p class="intro">One of the main reasons people don’t switch banks is that it can be a hassle. At Morvale Commerce Bank we make it easy. We value your time and with our efficient three step process, switching banks has never been easier.</p>

  <p class="welcome">We look forward to creating an exceptional experience for you at <strong>Morvale Commerce Bank</strong></p>

  <div class="band" style="top:274px"></div>

  <div class="step-badge" style="top:318px">1</div>
  <h2 class="step-title fit" style="left:57px;top:321px">Open a Morvale Commerce Bank Account</h2>
  <p class="step-text dark" style="left:28px;top:355px;width:342px">Stop by our branch and visit with our knowledgeable team to open your new account.</p>
  <p class="step-text dark" style="left:28px;top:385px;width:342px">We will be happy to assist you in choosing the right account for your banking needs.</p>
  <div class="photo meeting" role="img" aria-label="Photo of a banker and customer reviewing paperwork beside a laptop"></div>

  <div class="band" style="top:447px"></div>

  <div class="step-badge" style="top:466px">2</div>
  <h2 class="step-title" style="left:60px;top:468px;width:548px;text-align:center">Stop using your old account and redirect your automatic payments and direct deposits.</h2>
  <p class="step-text navy" style="left:28px;top:521px;width:580px;text-align:center">It is important to remember to keep your old account open to ensure all your outstanding checks, deposits, and automatic withdrawals have cleared.</p>

  <div class="band" style="top:561px"></div>

  <div class="step-badge" style="top:603px">3</div>
  <h2 class="step-title" style="left:61px;top:605px">Close your old account</h2>
  <p class="step-text navy" style="left:28px;top:642px;width:335px">Now you are ready to switch. We will even provide an Account Closure Authorization form to close your old account. Any remaining account balance will be transferred to your Morvale Commerce Bank account.</p>
  <div class="photo atm" role="img" aria-label="Photo of a customer using an outdoor ATM"></div>

  <footer class="footer">
    <svg class="pin-icon" width="26" height="44" viewBox="0 0 26 44" aria-hidden="true">
      <path d="M13 2C7.5 2 4 6 4 11c0 6 9 18 9 18s9-12 9-18c0-5-3.5-9-9-9z" fill="none" stroke="#fff" stroke-width="2.4"/>
      <circle cx="13" cy="11" r="3.6" fill="none" stroke="#fff" stroke-width="2.2"/>
      <ellipse cx="13" cy="37" rx="12" ry="4" fill="none" stroke="#fff" stroke-width="1.8"/>
    </svg>
    <div class="address">2740 North Harlow Avenue,<br>Suite 310<br>Fernbrook, AZ 85260</div>
    <svg class="phone-icon" width="40" height="40" viewBox="0 0 40 40" aria-hidden="true">
      <path d="M9 6l6 8-3 4c2 5 6 9 11 11l4-3 8 6-4 5C19 37 4 22 4 10z" fill="none" stroke="#fff" stroke-width="2.6" stroke-linejoin="round"/>
      <path d="M22 12a7 7 0 0 1 6 6M23 6a13 13 0 0 1 11 11M24 1a19 19 0 0 1 15 15" fill="none" stroke="#fff" stroke-width="2.2" stroke-linecap="round"/>
    </svg>
    <div class="phone">480.555.0142</div>
  </footer>
</main>
</body>
</html>
```